Flyer Design in Photoshop PSD format needed

Christmas Production Flyer - DL (Horizontal) 210 wide x 100 deep

Final file to have elements as layered .psd

We need a flyer design to promote our upcoming Christmas Production which will be based on a movie premier.

Target Market(s)

Young Families Young Adult

Industry/Entity Type

Movie

Requirements
Must have
• The design should look like a Movie poster or Movie Premier advertisement.
Movie Title: Lantern (Main line, focal point) of Tidings (Tag line, possibly italicised)
Dates: 16th and 18th of December
Time: 7pm
Tickets: Booking Online
Price: Free
Address: The Marlowe 412 Wattle St Newcastle
Presented by - Fellowship72

In the strip at the bottom
Parking available at Corvel and Rest Harbour
Starring: Baby Jesus, Mary, Joseph, Gabriel, Choir of Angels

(Colours - midnight style theme/night sky/stars - not heaps of colour - dramatic)
Nice to have
• Theme:
Like as on movie posters e.g. starring. Valmont Screen Gala premier glitz and glam. Monaco.
Star sitting above middle (left to right) shining down onto a manger
Black strip at the bottom like in a movie poster containing most of the info regarding the event.
Should not have
• Snow
Christmas Tree, bobbles and presents, tinsel not kitch

```html
<!DOCTYPE html>
<html lang="en">
<head>
<meta charset="utf-8">
<title>Lantern of Tidings – Christmas Production Flyer</title>
<link rel="stylesheet" href="https://fonts.googleapis.com/css2?family=Dancing+Script:wght@700&family=Cormorant+Garamond:ital,wght@0,700;1,700&family=Cormorant+SC:wght@600;700&family=Archivo+Narrow:wght@700&display=swap">
<style>
  :root {
    --canvas: #e1c99b;
    --night: #1d1f17;
    --moss: #4a4f3a;
    --gold: #f6ea72;
    --white: #ffffff;
    --cocoa: #4a2c1c;
    --cocoa-dark: #3a2216;
    --ash: #3b3a33;
    --cream: #efe6cc;
  }
  * { box-sizing: border-box; margin: 0; padding: 0; }
  html, body { width: 1200px; height: 900px; overflow: hidden; background: var(--canvas); }
  .canvas { position: relative; width: 1200px; height: 900px; }

  .flyer {
    position: absolute; left: 376px; top: 30px; width: 420px; height: 834px;
    overflow: hidden; background: var(--night);
  }
  .scene {
    position: absolute; inset: 0;
    background:
      radial-gradient(ellipse 60% 22% at 50% 62%, rgba(240,240,235,0.55), transparent 70%),
      radial-gradient(ellipse 70% 30% at 45% 66%, rgba(120,90,50,0.7), transparent 75%),
      radial-gradient(ellipse 35% 18% at 0% 10%, rgba(150,150,140,0.35), transparent 70%),
      radial-gradient(ellipse 35% 18% at 100% 10%, rgba(150,150,140,0.35), transparent 70%),
      linear-gradient(180deg, #1a1c15 0%, #2b3024 25%, var(--moss) 50%, #4f4e3c 70%, #3a3830 100%);
  }
  .star-glow {
    position: absolute; left: 114px; top: -20px; width: 200px; height: 170px;
    background: radial-gradient(circle at 50% 47%, #fffbe0 0 4%, rgba(250,230,120,0.9) 8%, rgba(230,190,60,0.35) 28%, transparent 60%);
  }

  .title-block { position: absolute; left: 0; top: 0; width: 100%; color: var(--gold); font-family: "Dancing Script", cursive; text-shadow: 0 2px 6px rgba(0,0,0,0.5); }
  .title-main {
    position: absolute; left: 0; top: 128px; width: 100%; text-align: center;
    font-size: 98px; line-height: 1; font-weight: 700;
  }
  .title-of {
    position: absolute; left: 318px; top: 234px; font-size: 34px; line-height: 1;
  }
  .title-tag {
    position: absolute; left: 40px; top: 262px; width: 380px; text-align: center;
    font-size: 52px; line-height: 1; font-weight: 700;
  }

  .cast { position: absolute; left: 0; top: 350px; width: 100%; text-align: center; color: var(--white); }
  .cast-label { font-family: "Cormorant Garamond", serif; font-style: italic; font-weight: 700; font-size: 22px; }
  .cast-names { font-family: "Cormorant SC", serif; font-weight: 700; font-size: 20px; line-height: 26px; margin-top: 2px; }

  .info-band {
    position: absolute; left: 0; top: 704px; width: 100%; height: 50px;
    background: linear-gradient(90deg, var(--cocoa-dark), var(--cocoa));
    padding: 6px 0 0 26px; color: var(--cream);
    font-family: "Archivo Narrow", sans-serif; font-size: 14px; line-height: 19px;
  }
  .info-band .dot { margin: 0 6px; }

  .footer {
    position: absolute; left: 0; top: 754px; width: 100%; height: 80px;
    background: linear-gradient(180deg, rgba(59,58,51,0.4), var(--ash) 40%);
    text-align: center; padding-top: 18px; color: var(--cream);
    font-family: "Cormorant SC", serif; font-weight: 600; font-size: 17px; line-height: 22px;
  }

  .price-badge {
    position: absolute; z-index: 2; left: 252px; top: 646px; width: 132px; height: 132px; border-radius: 50%;
    background: var(--cocoa); border: 2px solid rgba(255,255,255,0.15);
    display: flex; flex-direction: column; align-items: center; justify-content: center;
    color: var(--white); text-align: center;
  }
  .price-badge .price { font-family: "Cormorant Garamond", serif; font-weight: 700; font-size: 40px; line-height: 1; }
  .price-badge .note { font-family: "Archivo Narrow", sans-serif; font-size: 13px; line-height: 14px; margin-top: 2px; color: var(--white); }
</style>
</head>
<body>
<div class="canvas">
  <section class="flyer">
    <div class="scene" role="img" aria-label="Night scene with a straw-filled wooden manger lit from above, soft smoke at the top corners"></div>
    <div class="star-glow" role="img" aria-label="Bright shining star above the manger"></div>

    <header class="title-block">
      <h1 class="title-main">Lantern</h1>
      <span class="title-of">of</span>
      <h2 class="title-tag">Tidings</h2>
    </header>

    <div class="cast">
      <p class="cast-label">Starring:</p>
      <p class="cast-names">Baby Jesus, Mary, Joseph, Gabriel,<br>Choir of Angels</p>
    </div>

    <div class="info-band">
      <p>16th and 18th of December<span class="dot">•</span>7.00 PM</p>
      <p>The Marlowe 412 Wattle St Newcastle</p>
    </div>

    <footer class="footer">
      <p>Parking Available at Corvel and Rest Harbour</p>
      <p>Presented By: Fellowship72</p>
    </footer>

    <div class="price-badge">
      <span class="price">FREE</span>
      <span class="note">Tickets<br>Booking<br>Online</span>
    </div>
  </section>
</div>
</body>
</html>
```